MSA Plans

I would like to rebuild my brochure for the 3 business plans that I currently offer my clients. I would like to make it look much more modern & attractive to clients when choosing one of our service plans. If we can stick to a tech theme that would be great. Message me for anymore information.

```html
<!DOCTYPE html>
<html lang="en">
<head>
<meta charset="utf-8">
<title>Northdesk – Service Plans</title>
<link href="https://fonts.googleapis.com/css2?family=Montserrat:wght@300;400;500;600;700;800&display=swap" rel="stylesheet">
<style>
:root{
  --orange:#f4613f;
  --red:#e8312b;
  --red-deep:#c41e22;
  --ink:#262626;
  --dark:#1c1c1c;
  --cell:#3a3a3a;
  --cell-line:#2b2b2b;
  --tick:#3ccf5a;
  --freq:#f07a3a;
  --annual:#9bc23c;
  --peach:#fde2d8;
  --text:#333;
}
*{box-sizing:border-box;margin:0;padding:0}
html,body{width:1200px;height:4386px;overflow:hidden}
body{background:#fff;font-family:'Montserrat',sans-serif;position:relative}
.page{position:absolute;left:109px;width:979px;overflow:hidden}
.page-msa{top:1351px;height:1381px;background:linear-gradient(180deg,#242424 0%,#2e2e2e 60%,#2a2a2a 88%,#c0422c 94%,var(--orange) 100%)}
.page-cyber{top:2791px;height:1383px;background:linear-gradient(165deg,var(--orange) 0%,#f05a3a 35%,#8a3526 55%,#2a2424 72%,#1e1e1e 100%)}
.brand{position:absolute;left:59px;top:42px;display:flex;align-items:center;gap:10px;color:#fff;font-weight:700;font-size:24px;letter-spacing:1px}
.brand-mark{width:20px;height:20px;background:var(--red)}
.version{position:absolute;right:58px;top:44px;color:#ddd;font-size:12px;letter-spacing:1px}
.page-title{position:absolute;left:59px;top:126px;color:var(--orange);font-weight:800;font-size:30px;line-height:34px;letter-spacing:1px}
.page-intro{position:absolute;right:46px;top:150px;color:#fff;font-size:16px;line-height:21px;letter-spacing:1.5px;text-align:right;font-weight:400}

/* Plan table */
.plan-table{position:absolute;display:grid}
.msa-table{left:39px;top:235px;grid-template-columns:377px 158px 158px 158px;column-gap:22px}
.cyber-table{left:59px;top:154px;grid-template-columns:449px 183px 183px;column-gap:24px}
.cell{display:flex;align-items:center;justify-content:center;text-align:center}
.label{color:var(--text);font-size:13px;font-weight:500;letter-spacing:.6px;background:#fff;border-bottom:1px solid #f1d6cc;line-height:18px}
.val{background:var(--cell);border-bottom:1px solid var(--cell-line);font-size:11px;letter-spacing:1px;font-weight:500}
.r28{height:28px}
.sec-label{background:linear-gradient(180deg,#fff,var(--peach));align-items:flex-end;padding-bottom:12px}
.sec-val{background:var(--dark)}
.pill{background:var(--red);color:#fff;font-size:13px;font-weight:600;letter-spacing:1px;padding:3px 0;width:164px;border-radius:2px}
.vip{color:#f0533a}
.freq{color:var(--freq)}
.annual{color:var(--annual)}
.level{color:var(--tick);font-size:13px}
.pending{color:var(--tick);font-size:12px;line-height:14px}
.tick,.cross{width:22px;height:22px}

.panel-head{background:linear-gradient(180deg,#242424 0%,#4a4a4a 70%,#e6e6e6 100%);border-radius:18px 18px 0 0;color:#fff;font-weight:300;font-size:24px;letter-spacing:3px;line-height:30px}
.plan-head{background:var(--dark);border-radius:14px 14px 0 0;flex-direction:column;justify-content:flex-start;overflow:hidden}
.plan-tab{width:100%;background:var(--red);color:#fff;font-weight:700;font-size:15px;letter-spacing:1px;padding:14px 0 10px;text-align:center}
.plan-price{width:100%;background:linear-gradient(180deg,#e83a2c 0%,#f0563a 55%,var(--red-deep) 100%);border-radius:0 0 28px 28px;color:#fff;text-align:center;padding:14px 0 22px;box-shadow:0 10px 14px rgba(0,0,0,.55)}
.amount{font-size:44px;font-weight:600;letter-spacing:1px;line-height:46px}
.amount sup{font-size:18px;vertical-align:22px;margin-right:2px}
.commit{font-size:7px;letter-spacing:.5px;opacity:.9}

.panel-foot{background:#111;border-radius:0 0 18px 18px;flex-direction:column;gap:22px;color:#f0533a;font-size:14px;letter-spacing:.5px;justify-content:center}
.plan-foot{background:#111;border-radius:0 0 14px 14px;flex-direction:column;gap:22px;color:#fff;font-size:18px;font-weight:600}
.plan-foot sup{font-size:10px}

/* Cybersecurity page */
.cyber-head{background:linear-gradient(180deg,#333 0%,#e9e9e9 22%,#fff 55%,#fff 100%);border-radius:16px 16px 0 0;color:#151515;font-weight:300;font-size:48px;letter-spacing:5px;line-height:58px;justify-content:flex-start;align-items:flex-start;text-align:left;padding:34px 0 0 26px}
.cyber-table .label{font-size:15px;line-height:21px;background:linear-gradient(90deg,#fff,#fff7f4)}
.cyber-table .val{background:#333;border-bottom:1px solid #262626}
.r42{height:42px}
.r64{height:64px}
.cyber-foot-label{background:linear-gradient(180deg,#fff,var(--peach));border-radius:0 0 14px 14px;flex-direction:column;gap:24px;color:#f0533a;font-size:14px;justify-content:center}
.cyber-table .plan-foot{background:#333;border-radius:0 0 14px 14px}
.cyber-table .plan-head{background:#262626}

.company{position:absolute;left:59px;top:1287px;color:#fff;font-size:11px;letter-spacing:1px;line-height:16px}
.company strong{color:var(--orange);font-weight:600;display:block;margin-bottom:6px}
.company div{display:flex;align-items:center;gap:6px}
.company svg{width:11px;height:11px}
.dot-field{position:absolute;right:40px;top:1285px;width:170px;height:72px;background:#1f1f1f}
</style>
</head>
<body>
<svg width="0" height="0" style="position:absolute">
  <symbol id="tick" viewBox="0 0 24 24"><path d="M4 12.5l5 5L20 6.5" fill="none" stroke="#3ccf5a" stroke-width="3.2" stroke-linecap="round" stroke-linejoin="round"/></symbol>
  <symbol id="cross" viewBox="0 0 24 24"><path d="M7 7l10 10M17 7L7 17" fill="none" stroke="#e8312b" stroke-width="3" stroke-linecap="round"/></symbol>
</svg>

<!-- Managed Service Framework -->
<section class="page page-msa">
  <div class="brand"><span class="brand-mark"></span>NORTHDESK</div>
  <div class="version">V1.0. APR 24</div>
  <h1 class="page-title">MANAGED<br>SERVICE FRAMEWORK</h1>
  <p class="page-intro">Defining our services and how<br>we deliver these consistently to you</p>

  <div class="plan-table msa-table">
    <div class="cell panel-head" style="height:176px">Managed Services<br>Agreement</div>
    <div class="cell plan-head"><div class="plan-tab">ESSENTIAL</div><div class="plan-price"><div class="amount"><sup>$</sup>550</div><div class="commit">Minimum Monthly Commit</div></div></div>
    <div class="cell plan-head"><div class="plan-tab">BUSINESS</div><div class="plan-price"><div class="amount"><sup>$</sup>650</div><div class="commit">Minimum Monthly Commit</div></div></div>
    <div class="cell plan-head"><div class="plan-tab">PROFESSIONAL</div><div class="plan-price"><div class="amount"><sup>$</sup>825</div><div class="commit">Minimum Monthly Commit</div></div></div>

    <div class="cell label sec-label" style="height:40px;padding-bottom:8px"><span class="pill">Support</span></div>
    <div class="cell val sec-val"></div><div class="cell val sec-val"></div><div class="cell val sec-val"></div>
    <div class="cell label r28">Unlimited Remote Support 7am - 6pm</div>
    <div class="cell val"><svg class="tick"><use href="#tick"/></svg></div><div class="cell val"><svg class="tick"><use href="#tick"/></svg></div><div class="cell val"><svg class="tick"><use href="#tick"/></svg></div>
    <div class="cell label r28">3rd Party Vendor Support</div>
    <div class="cell val"><svg class="tick"><use href="#tick"/></svg></div><div class="cell val"><svg class="tick"><use href="#tick"/></svg></div><div class="cell val"><svg class="tick"><use href="#tick"/></svg></div>
    <div class="cell label r28">Reactive Onsite Support 8am - 5pm*</div>
    <div class="cell val vip">VIP RATES</div><div class="cell val"><svg class="tick"><use href="#tick"/></svg></div><div class="cell val"><svg class="tick"><use href="#tick"/></svg></div>
    <div class="cell label r28">After-Hours Support*</div>
    <div class="cell val vip">VIP RATES</div><div class="cell val vip">VIP RATES</div><div class="cell val"><svg class="tick"><use href="#tick"/></svg></div>

    <div class="cell label sec-label" style="height:59px"><span class="pill">Service</span></div>
    <div class="cell val sec-val"></div><div class="cell val sec-val"></div><div class="cell val sec-val"></div>
    <div class="cell label r28">Guaranteed SLA Response times</div>
    <div class="cell val"><svg class="tick"><use href="#tick"/></svg></div><div class="cell val"><svg class="tick"><use href="#tick"/></svg></div><div class="cell val"><svg class="tick"><use href="#tick"/></svg></div>
    <div class="cell label r28">24/7 Website &amp; Infrastructure Monitoring</div>
    <div class="cell val"><svg class="tick"><use href="#tick"/></svg></div><div class="cell val"><svg class="tick"><use href="#tick"/></svg></div><div class="cell val"><svg class="tick"><use href="#tick"/></svg></div>
    <div class="cell label r28">Secure Web Content Filtering</div>
    <div class="cell val"><svg class="tick"><use href="#tick"/></svg></div><div class="cell val"><svg class="tick"><use href="#tick"/></svg></div><div class="cell val"><svg class="tick"><use href="#tick"/></svg></div>
    <div class="cell label r28">Backup Monitoring</div>
    <div class="cell val"><svg class="tick"><use href="#tick"/></svg></div><div class="cell val"><svg class="tick"><use href="#tick"/></svg></div><div class="cell val"><svg class="tick"><use href="#tick"/></svg></div>
    <div class="cell label r28">Operating System Patching &amp; Updating</div>
    <div class="cell val"><svg class="tick"><use href="#tick"/></svg></div><div class="cell val"><svg class="tick"><use href="#tick"/></svg></div><div class="cell val"><svg class="tick"><use href="#tick"/></svg></div>
    <div class="cell label r28">CEO / MD Home Tech Support</div>
    <div class="cell val"><svg class="tick"><use href="#tick"/></svg></div><div class="cell val"><svg class="tick"><use href="#tick"/></svg></div><div class="cell val"><svg class="tick"><use href="#tick"/></svg></div>
    <div class="cell label r28">Monthly Tech Site Visit</div>
    <div class="cell val"><svg class="cross"><use href="#cross"/></svg></div><div class="cell val freq">QUARTERLY</div><div class="cell val freq">MONTHLY</div>
    <div class="cell label r28">Short Term Loan Equipment</div>
    <div class="cell val"><svg class="cross"><use href="#cross"/></svg></div><div class="cell val freq">1 MONTH</div><div class="cell val freq">3 MONTH</div>
    <div class="cell label r28">Adds / Moves / Changes (Staff)</div>
    <div class="cell val"><svg class="tick"><use href="#tick"/></svg></div><div class="cell val"><svg class="tick"><use href="#tick"/></svg></div><div class="cell val"><svg class="tick"><use href="#tick"/></svg></div>
    <div class="cell label r28">Adds / Moves / Changes (Workstation)</div>
    <div class="cell val vip">VIP RATES</div><div class="cell val vip">VIP RATES</div><div class="cell val"><svg class="tick"><use href="#tick"/></svg></div>

    <div class="cell label sec-label" style="height:59px"><span class="pill">Management</span></div>
    <div class="cell val sec-val"></div><div class="cell val sec-val"></div><div class="cell val sec-val"></div>
    <div class="cell label r28">Asset and Warranty Tracking &amp; Reporting</div>
    <div class="cell val"><svg class="tick"><use href="#tick"/></svg></div><div class="cell val"><svg class="tick"><use href="#tick"/></svg></div><div class="cell val"><svg class="tick"><use href="#tick"/></svg></div>
    <div class="cell label r28">Comprehensive IT Documentation</div>
    <div class="cell val"><svg class="tick"><use href="#tick"/></svg></div><div class="cell val"><svg class="tick"><use href="#tick"/></svg></div><div class="cell val"><svg class="tick"><use href="#tick"/></svg></div>
    <div class="cell label r28">Tech. Strategy Meeting*</div>
    <div class="cell val annual">ANNUAL</div><div class="cell val freq">QUARTERLY</div><div class="cell val freq">MONTHLY</div>
    <div class="cell label r28">Tech. Business Reviewing Meeting*</div>
    <div class="cell val annual">ANNUAL</div><div class="cell val freq">BI ANNUAL</div><div class="cell val freq">QUARTERLY</div>
    <div class="cell label r28">IT Policy Templates</div>
    <div class="cell val"><svg class="cross"><use href="#cross"/></svg></div><div class="cell val"><svg class="tick"><use href="#tick"/></svg></div><div class="cell val"><svg class="tick"><use href="#tick"/></svg></div>

    <div class="cell label sec-label" style="height:59px"><span class="pill">Training</span></div>
    <div class="cell val sec-val"></div><div class="cell val sec-val"></div><div class="cell val sec-val"></div>
    <div class="cell label r28">End User Training Materials</div>
    <div class="cell val"><svg class="cross"><use href="#cross"/></svg></div><div class="cell val"><svg class="tick"><use href="#tick"/></svg></div><div class="cell val"><svg class="tick"><use href="#tick"/></svg></div>
    <div class="cell label r28">Security Awareness Training</div>
    <div class="cell val"><svg class="tick"><use href="#tick"/></svg></div><div class="cell val"><svg class="cross"><use href="#cross"/></svg></div><div class="cell val"><svg class="tick"><use href="#tick"/></svg></div>

    <div class="cell panel-foot" style="height:140px"><span>RPP/User</span><span>Minimum User Count</span></div>
    <div class="cell plan-foot"><span><sup>$</sup>110</span><span>5</span></div>
    <div class="cell plan-foot"><span><sup>$</sup>130</span><span>5</span></div>
    <div class="cell plan-foot"><span><sup>$</sup>165</span><span>5</span></div>
  </div>
</section>

<!-- Cybersecurity Packages -->
<section class="page page-cyber">
  <div class="brand" style="top:38px"><span class="brand-mark" style="background:#fff"></span>NORTHDESK</div>
  <div class="version" style="top:40px;color:#fff">V1.0. APR 24</div>

  <div class="plan-table cyber-table">
    <div class="cell cyber-head" style="height:233px">Cybersecurity<br>Packages</div>
    <div class="cell plan-head"><div class="plan-tab" style="padding:18px 0 12px">BUSINESS</div><div class="plan-price"><div class="amount"><sup>$</sup>175</div><div class="commit">Minimum Monthly Commit</div></div></div>
    <div class="cell plan-head"><div class="plan-tab" style="padding:18px 0 12px">PROFESSIONAL</div><div class="plan-price"><div class="amount"><sup>$</sup>650</div><div class="commit">Minimum Monthly Commit</div></div></div>

    <div class="cell label r42">Compliance with NCSB Essential 8 Maturity*</div>
    <div class="cell val level">LEVEL 0</div><div class="cell val level">LEVEL 1</div>
    <div class="cell label r64">Security Standard - Alignment to Northdesk Cloud<br>Security Policy &amp; Reporting</div>
    <div class="cell val"><svg class="tick"><use href="#tick"/></svg></div><div class="cell val"><svg class="tick"><use href="#tick"/></svg></div>
    <div class="cell label r64">24/7 Security Operations Centre (SOC)<br>Monitoring Cloud Office Suite</div>
    <div class="cell val"><svg class="tick"><use href="#tick"/></svg></div><div class="cell val"><svg class="tick"><use href="#tick"/></svg></div>
    <div class="cell label r42">Dark Web Scanning</div>
    <div class="cell val"><svg class="tick"><use href="#tick"/></svg></div><div class="cell val"><svg class="tick"><use href="#tick"/></svg></div>
    <div class="cell label r42">Cloud Email Filtering</div>
    <div class="cell val"><svg class="tick"><use href="#tick"/></svg></div><div class="cell val"><svg class="tick"><use href="#tick"/></svg></div>
    <div class="cell label r42">Cloud Suite Backup</div>
    <div class="cell val"><svg class="tick"><use href="#tick"/></svg></div><div class="cell val"><svg class="tick"><use href="#tick"/></svg></div>
    <div class="cell label r42">Automated Email Signatures</div>
    <div class="cell val"><svg class="tick"><use href="#tick"/></svg></div><div class="cell val"><svg class="tick"><use href="#tick"/></svg></div>
    <div class="cell label r64">Endpoint Protection with EDR<br>Workstations &amp; Servers</div>
    <div class="cell val"><svg class="tick"><use href="#tick"/></svg></div><div class="cell val"><svg class="tick"><use href="#tick"/></svg></div>
    <div class="cell label r42">3rd Party Applications Updating</div>
    <div class="cell val"><svg class="cross"><use href="#cross"/></svg></div><div class="cell val"><svg class="tick"><use href="#tick"/></svg></div>
    <div class="cell label r64">24/7 Security Operations Centre (SOC)<br>Monitoring Endpoints and Servers</div>
    <div class="cell val"><svg class="cross"><use href="#cross"/></svg></div><div class="cell val"><svg class="tick"><use href="#tick"/></svg></div>
    <div class="cell label r64">Privileged Access Management &amp;<br>Application Whitelisting</div>
    <div class="cell val"><svg class="cross"><use href="#cross"/></svg></div><div class="cell val"><svg class="tick"><use href="#tick"/></svg></div>
    <div class="cell label r42">Internal Vulnerability Scanning</div>
    <div class="cell val"><svg class="cross"><use href="#cross"/></svg></div><div class="cell val"><svg class="tick"><use href="#tick"/></svg></div>
    <div class="cell label r64">Backup &amp; Disaster Recovery to comply<br>with NCSB Essential 8 Maturity Level 1</div>
    <div class="cell val"><svg class="cross"><use href="#cross"/></svg></div><div class="cell val pending">PENDING<br>ASSESSMENT</div>

    <div class="cell cyber-foot-label" style="height:161px"><span>RPP/User</span><span>Minimum User Count</span></div>
    <div class="cell plan-foot"><span><sup>$</sup>35</span><span>5</span></div>
    <div class="cell plan-foot"><span><sup>$</sup>60</span><span>5</span></div>
  </div>

  <div class="company">
    <strong>NORTHDESK IT SERVICES PTY LTD | ABN: 00 000 000 000</strong>
    <div><svg viewBox="0 0 12 12"><circle cx="5" cy="5" r="3.5" fill="none" stroke="#f4613f" stroke-width="1.4"/><path d="M7.5 7.5l3 3" stroke="#f4613f" stroke-width="1.4"/></svg>northdeskit.com.au</div>
    <div><svg viewBox="0 0 12 12"><rect x="1" y="2.5" width="10" height="7" fill="none" stroke="#f4613f" stroke-width="1.2"/><path d="M1 3l5 4 5-4" fill="none" stroke="#f4613f" stroke-width="1.2"/></svg>hello@northdeskit.com.au</div>
    <div><svg viewBox="0 0 12 12"><path d="M6 11S2 7 2 4.5a4 4 0 018 0C10 7 6 11 6 11z" fill="none" stroke="#f4613f" stroke-width="1.3"/><circle cx="6" cy="4.5" r="1.3" fill="#f4613f"/></svg>14 Harlow St, Elmvale, VIC, 3999 | 1300 000 555</div>
  </div>
  <div class="dot-field" role="img" aria-label="Decorative grid of small red dots"></div>
</section>
</body>
</html>
```